Construction material supplies company business card ****

1. Full company name “K R Mortar Works Ltd”
I am after a Business card design for the company as a whole. We are better known in Solomon Islands as “K R Mortar” for short.

We are a building materials supplier of
Ready Mixed Concrete, Bricks and Blocks,
Quarry products- gravel, aggregates, sand etc.
Cement distributor/retailer of reputable brands.
Other prefab concrete products. Culverts, wave breakers, concrete retaining blocks etc.

2. Competitive Advantage over Competition: Quality, efficient, professional, dependable, reliable

3. We want people to feel trust worthy, high quality, strong when they see our brand

5. No preference to color. Maybe more sturdy and corporate. Not fancy.

Industry/Entity Type

CONSTRUCTION SUPPLY

Contact Information for Business Card

Name, Position, office phone mob phone, email

Requirements
Must have
• the company logo
Nice to have
• would like to see a mixture of designs, of with logo only and also with simple graphic designs to bring out the company whilst still have the strong sturdy professional feeling

```html
<!DOCTYPE html>
<html lang="en">
<head>
<meta charset="utf-8">
<title>K R Mortar Works Ltd — Business Card</title>
<link href="https://fonts.googleapis.com/css2?family=Michroma&family=Open+Sans:wght@400&display=swap" rel="stylesheet">
<style>
  :root {
    --backdrop: #2b2b2b;
    --card-blue: #134566;
    --card-blue-light: #1c5478;
    --ink-white: #ffffff;
    --card-w: 620px;
    --card-h: 354px;
  }
  * { box-sizing: border-box; margin: 0; padding: 0; }
  html, body {
    width: 1200px;
    height: 900px;
    overflow: hidden;
    background: var(--backdrop);
  }
  .canvas {
    position: relative;
    width: 1200px;
    height: 900px;
    display: flex;
    flex-direction: column;
    align-items: center;
    justify-content: center;
    gap: 48px;
  }
  .card {
    position: relative;
    width: var(--card-w);
    height: var(--card-h);
    background: linear-gradient(100deg, var(--card-blue) 0%, var(--card-blue) 55%, var(--card-blue-light) 100%);
    color: var(--ink-white);
  }

  /* Front: company name lockup */
  .card--front {
    display: flex;
    align-items: center;
    justify-content: center;
  }
  .brand {
    display: flex;
    flex-direction: column;
    align-items: center;
    gap: 16px;
  }
  .brand__mark {
    width: 44px;
    height: 44px;
    border: 4px solid var(--ink-white);
  }
  .brand__name {
    font-family: "Michroma", sans-serif;
    font-size: 26px;
    letter-spacing: 2px;
    text-transform: uppercase;
    text-align: center;
    line-height: 1.35;
  }

  /* Back: person + contacts */
  .card--back {
    display: flex;
    align-items: center;
    padding-left: 48px;
  }
  .person {
    width: 280px;
    text-align: right;
  }
  .person__name {
    font-family: "Michroma", sans-serif;
    font-size: 22px;
    letter-spacing: 1px;
    text-transform: uppercase;
    line-height: 1.2;
  }
  .person__role {
    font-family: "Open Sans", sans-serif;
    font-size: 15px;
    margin-top: 4px;
  }
  .divider {
    width: 1.5px;
    height: 54px;
    background: var(--ink-white);
    margin: 18px 0 0 24px;
  }
  .contacts {
    list-style: none;
    margin: 18px 0 0 22px;
    font-family: "Open Sans", sans-serif;
    font-size: 15px;
    line-height: 1.45;
  }
  .contacts__item {
    display: flex;
    align-items: center;
    gap: 10px;
  }
  .contacts__icon {
    width: 13px;
    height: 13px;
    flex: none;
  }
</style>
</head>
<body>
<main class="canvas">
  <section class="card card--front" aria-label="Card front">
    <div class="brand">
      <div class="brand__mark"></div>
      <h1 class="brand__name">K R Mortar<br>Works Ltd</h1>
    </div>
  </section>

  <section class="card card--back" aria-label="Card back">
    <div class="person">
      <h2 class="person__name">Daniel Hughes</h2>
      <p class="person__role">Founder and CEO</p>
    </div>
    <div class="divider"></div>
    <ul class="contacts">
      <li class="contacts__item">
        <svg class="contacts__icon" viewBox="0 0 16 16" aria-hidden="true">
          <path d="M3.5 1.5l2.5 3-1.5 1.8c.8 1.8 2.4 3.4 4.2 4.2L10.5 9l3 2.5-1.3 2.5C7 14 2 9 2 3.2z" fill="#fff"/>
        </svg>
        <span>000 000 0000</span>
      </li>
      <li class="contacts__item">
        <svg class="contacts__icon" viewBox="0 0 16 16" aria-hidden="true">
          <rect x="4" y="1" width="8" height="14" rx="1.5" fill="none" stroke="#fff" stroke-width="1.5"/>
          <line x1="7" y1="12.5" x2="9" y2="12.5" stroke="#fff" stroke-width="1.2"/>
        </svg>
        <span>000 000 0000</span>
      </li>
      <li class="contacts__item">
        <svg class="contacts__icon" viewBox="0 0 16 16" aria-hidden="true">
          <rect x="1" y="3" width="14" height="10" rx="1" fill="none" stroke="#fff" stroke-width="1.5"/>
          <polyline points="1.5,3.5 8,9 14.5,3.5" fill="none" stroke="#fff" stroke-width="1.5"/>
        </svg>
        <span>info@krmortar.com.au</span>
      </li>
    </ul>
  </section>
</main>
</body>
</html>
```